Business Card Design Project

Want a modern business card.
Concern is that our email address is long and thus poses a design challenge.
Items like the company name can be omitted from text as it will be available via the logo.

Example:
Desmond Farraway
President / CEO
Cell 555.304.2817
Office 555.619.0352
desmondf@qtvnetworkplatforms.example
www.qtvnetworkplatforms.example

Target Market(s)

Technical and executive level members of Information Technology companies in the Healthcare industry.

Industry/Entity Type

Business

Colors

Designer to choose colors to be used in the design.

Requirements
Nice to have
• Raised logo, but I am open.

```html
<!DOCTYPE html>
<html lang="en">
<head>
<meta charset="utf-8">
<title>QTV Network Platforms – Business Card</title>
<link rel="stylesheet" href="https://fonts.googleapis.com/css2?family=Arimo:wght@400;500&display=swap">
<style>
  :root {
    --page-bg: #e6e2dc;
    --card-white: #ffffff;
    --brand-blue: #2a4d8d;
    --brand-blue-light: #3b5f9f;
    --brand-red: #d8262f;
    --text-on-blue: #ffffff;
    --text-on-blue-soft: #d7e0ef;
    --card-shadow: rgba(40, 30, 20, 0.22);
  }
  * { margin: 0; padding: 0; box-sizing: border-box; }
  html, body {
    width: 1200px; height: 914px; overflow: hidden;
    background: var(--page-bg);
    font-family: "Arimo", Arial, sans-serif;
  }
  .sheet {
    width: 1200px; height: 914px;
    display: flex; flex-direction: column;
    align-items: center; justify-content: center; gap: 40px;
  }
  .card {
    position: relative;
    width: 700px; height: 400px;
    background: var(--card-white);
    box-shadow: 0 10px 28px var(--card-shadow);
    overflow: hidden;
  }
  .wordmark {
    font-family: "Arimo", Arial, sans-serif;
    font-weight: 500;
    color: var(--brand-blue);
    white-space: nowrap;
  }

  /* Back side */
  .card-back {
    display: flex; flex-direction: column;
    align-items: center; justify-content: center; gap: 18px;
  }
  .card-back .wordmark { font-size: 42px; }
  .card-back .site-url {
    color: var(--brand-red);
    font-size: 19px;
    letter-spacing: 0.3px;
  }

  /* Front side */
  .card-front .logo-area {
    position: absolute; left: 0; top: 0; right: 0; height: 150px;
    display: flex; align-items: center; justify-content: flex-end;
    padding-right: 56px;
  }
  .card-front .wordmark { font-size: 34px; }
  .band-rule {
    position: absolute; left: 0; right: 0; top: 152px;
    height: 2px; background: var(--brand-blue);
  }
  .info-band {
    position: absolute; left: 0; right: 0; top: 160px; bottom: 0;
    background: linear-gradient(135deg, var(--brand-blue-light), var(--brand-blue));
    color: var(--text-on-blue);
    display: flex; align-items: center;
  }
  .identity { width: 380px; padding-left: 40px; padding-right: 24px; }
  .identity .person-name { font-size: 25px; font-weight: 500; }
  .identity .person-title {
    font-size: 17px; color: var(--text-on-blue-soft); margin: 6px 0 12px;
  }
  .contact-line {
    display: flex; align-items: center; gap: 9px;
    font-size: 14px; line-height: 1.75; white-space: nowrap;
  }
  .contact-line svg { width: 14px; height: 14px; flex: none; fill: var(--text-on-blue); }
  .divider {
    width: 1px; height: 150px; flex: none;
    background: rgba(255, 255, 255, 0.55);
  }
  .contacts { padding-left: 30px; }
</style>
</head>
<body>
<main class="sheet">

  <section class="card card-back" aria-label="Card back">
    <div class="wordmark">QTV Network Platforms</div>
    <div class="site-url">www.qtvnetworkplatforms.example</div>
  </section>

  <section class="card card-front" aria-label="Card front">
    <div class="logo-area">
      <div class="wordmark">QTV Network Platforms</div>
    </div>
    <div class="band-rule"></div>
    <div class="info-band">
      <div class="identity">
        <div class="person-name">Desmond Farraway</div>
        <div class="person-title">President / CEO</div>
        <div class="contact-line">
          <svg viewBox="0 0 16 16" aria-hidden="true"><path d="M1 3h14v10H1z M1.8 3.6 8 8.6l6.2-5v1.2L8 9.8 1.8 4.8z" fill-rule="evenodd"/></svg>
          <span>desmondf@qtvnetworkplatforms.example</span>
        </div>
      </div>
      <div class="divider"></div>
      <div class="contacts">
        <div class="contact-line">
          <svg viewBox="0 0 16 16" aria-hidden="true"><circle cx="8" cy="5" r="3.4"/><path d="M1.5 15c0-3.6 2.9-5.6 6.5-5.6s6.5 2 6.5 5.6z"/></svg>
          <span>555.304.2817</span>
        </div>
        <div class="contact-line">
          <svg viewBox="0 0 16 16" aria-hidden="true"><path d="M3 1h10v14H9.5v-3h-3v3H3z M5 3v2h2V3z M9 3v2h2V3z M5 7v2h2V7z M9 7v2h2V7z" fill-rule="evenodd"/></svg>
          <span>555.619.0352</span>
        </div>
        <div class="contact-line">
          <svg viewBox="0 0 16 16" aria-hidden="true"><path d="M8 1a7 7 0 1 0 0 14A7 7 0 0 0 8 1zm0 1.4a5.6 5.6 0 0 1 0 11.2 5.6 5.6 0 0 1 0-11.2zM2.6 7.3h10.8v1.4H2.6zM7.3 2.4h1.4v11.2H7.3z" fill-rule="evenodd"/></svg>
          <span>www.qtvnetworkplatforms.example</span>
        </div>
      </div>
    </div>
  </section>

</main>
</body>
</html>
```